Business Card Design

Name: Dorian Halvik
Title : Mathematics Instructor
Dep. Department of Mathmatics

Four Lindale Court
Camarillo, California 93010-2416

T: 805-555-0142
Cell: 805-555-0179

Email: dorian.halvik033@pelmarcu.edu
Email: quickhalvik@zentomail.com

Reason: I don't know how to post my image on the web.

Reason: The design PDF can not be uplorded

Industry/Entity Type

Business

Requirements
Must have
• http://www.pelmarcu.edu/tc/web/styleguide/logos-images.htm

http://www.bentwoodpress.com/pelmarcu/bc/
Nice to have
• I have to use the logo and the format based on their format to some extent.
White back ground

But is there any way to make mine special?
raised ink or 3D logo?

```html
<!DOCTYPE html>
<html lang="en">
<head>
<meta charset="utf-8">
<title>Dorian Halvik — Business Card</title>
<link rel="stylesheet" href="https://fonts.googleapis.com/css2?family=Archivo:wght@700;900&family=Jost:wght@400;500&display=swap">
<style>
  :root {
    --backdrop: #3b2f28;
    --card: #ffffff;
    --ink: #111111;
    --red: #e3262b;
    --dept-red: #b8242a;
    --blue: #1f4f9a;
    --maroon: #5a1a1a;
    --ring: #fbe5dc;
    --pin: #7cb342;
    --phone: #8a6a3c;
    --mail: #2f8fd8;
  }
  html, body {
    margin: 0;
    width: 1200px;
    height: 1200px;
    overflow: hidden;
    background: var(--backdrop);
  }
  .card {
    position: absolute;
    left: 100px;
    top: 314px;
    width: 1000px;
    height: 572px;
    background: var(--card);
    overflow: hidden;
    box-shadow: 0 14px 40px rgba(0,0,0,.45);
  }
  .card-art {
    position: absolute;
    inset: 0;
  }
  .identity {
    position: absolute;
    left: 52px;
    top: 52px;
    font-family: "Archivo", Arial, sans-serif;
    text-transform: uppercase;
    line-height: 1;
  }
  .identity .name {
    margin: 0;
    font-weight: 900;
    font-size: 38px;
    color: var(--ink);
    letter-spacing: .5px;
  }
  .identity .title {
    margin: 6px 0 0;
    font-weight: 700;
    font-size: 25px;
    color: var(--red);
    letter-spacing: .3px;
  }
  .department {
    position: absolute;
    left: 640px;
    top: 36px;
    width: 300px;
    text-align: center;
    font-family: "Archivo", Arial, sans-serif;
    font-weight: 700;
  }
  .department .brand {
    display: flex;
    align-items: center;
    justify-content: center;
    gap: 10px;
    font-size: 34px;
    color: var(--red);
    letter-spacing: 1px;
  }
  .department .brand-dot {
    width: 16px;
    height: 16px;
    border-radius: 50%;
    background: var(--red);
  }
  .department .dept-name {
    margin: 14px 0 0;
    font-size: 21px;
    line-height: 1.15;
    color: var(--dept-red);
    text-transform: uppercase;
  }
  .contacts {
    position: absolute;
    left: 48px;
    top: 296px;
    font-family: "Jost", "Futura", sans-serif;
    font-weight: 500;
    font-size: 24px;
    line-height: 1.2;
    color: var(--ink);
  }
  .contact-row {
    display: flex;
    align-items: center;
    gap: 20px;
    margin-bottom: 22px;
  }
  .contact-row p { margin: 0; }
  .contact-row.address p { color: var(--maroon); }
  .contact-icon { width: 54px; height: 48px; flex: none; }
</style>
</head>
<body>
  <main class="card">
    <svg class="card-art" viewBox="0 0 1000 572" aria-hidden="true">
      <circle cx="250" cy="530" r="300" fill="none" stroke="var(--ring)" stroke-width="32"/>
      <polyline points="0,150 560,150 650,215 1000,215" fill="none" stroke="var(--red)" stroke-width="7"/>
      <polyline points="0,165 554,165 644,230 1000,230" fill="none" stroke="var(--blue)" stroke-width="5"/>
    </svg>

    <header class="identity">
      <h1 class="name">Dorian Halvik</h1>
      <p class="title">Mathematics Instructor</p>
    </header>

    <aside class="department">
      <div class="brand"><span class="brand-dot"></span>PELMARCU</div>
      <p class="dept-name">Department of<br>Mathmatics</p>
    </aside>

    <section class="contacts">
      <div class="contact-row address">
        <svg class="contact-icon" viewBox="0 0 50 44" aria-hidden="true">
          <path d="M2 2h38v14l8 6-8 6v14H2z" fill="var(--pin)"/>
          <path d="M21 10a7 7 0 0 1 7 7c0 5-7 13-7 13s-7-8-7-13a7 7 0 0 1 7-7z" fill="#fff"/>
          <circle cx="21" cy="17" r="3" fill="var(--pin)"/>
        </svg>
        <p>Four Lindale Court<br>Camarillo, California 93010-2416</p>
      </div>
      <div class="contact-row">
        <svg class="contact-icon" viewBox="0 0 50 44" aria-hidden="true">
          <path d="M2 2h38v14l8 6-8 6v14H2z" fill="var(--phone)"/>
          <path d="M14 11c2-2 4-1 5 1l2 3c1 2 0 3-1 4 1 3 3 5 6 6 1-1 2-2 4-1l3 2c2 1 2 3 1 5-2 3-6 3-10 1-5-3-8-7-10-11-1-4-1-8 0-10z" fill="#fff"/>
        </svg>
        <p>Phone: 805-555-0142<br>Cell: 805-555-0179</p>
      </div>
      <div class="contact-row">
        <svg class="contact-icon" viewBox="0 0 50 44" aria-hidden="true">
          <path d="M2 2h38v14l8 6-8 6v14H2z" fill="var(--mail)"/>
          <rect x="10" y="13" width="22" height="16" fill="none" stroke="#fff" stroke-width="2"/>
          <polyline points="10,13 21,22 32,13" fill="none" stroke="#fff" stroke-width="2"/>
        </svg>
        <p>Email: dorian.halvik033@pelmarcu.edu<br>Email: quickhalvik@zentomail.com</p>
      </div>
    </section>
  </main>
</body>
</html>
```